" A Vela Frota Car tem como proposta oferecer soluçoes práticas e modernas na gestao, locaçao e terceirizaçao de frotas em todo Brasil, tendo como diferenciais flexibilidade, qualidade e agilidade, trazendo alternativas para cada tipo de cliente e aliando suas necessidades às açoes práticas de sustentabilidade e preservaçao do meio-ambiente, através da neutralizaçao de CO2 emitido por sua operaçao. "

```html
<!DOCTYPE html>
<html lang="pt-BR">
<head>
<meta charset="UTF-8">
<title>Vela Frota Car — Cartão de visita</title>
<link rel="stylesheet" href="https://fonts.googleapis.com/css2?family=Roboto+Condensed:wght@400;700&family=Cousine&display=swap">
<style>
  :root{
    --bg:#ececec;
    --blue-deep:#0a3f9c;
    --blue-mid:#1566d0;
    --blue-light:#3d9cf0;
    --green:#4aa31e;
    --green-dark:#2f7a10;
    --navy:#1d3f8f;
    --ink:#555;
    --white:#ffffff;
    --paper:#fafafa;
    --rule:#cfcfcf;
  }
  *{box-sizing:border-box;margin:0;padding:0}
  html,body{width:1200px;height:1200px;overflow:hidden}
  body{background:var(--bg);font-family:"Roboto Condensed",sans-serif;position:relative}
  .card{position:absolute;left:138px;width:924px;height:360px;overflow:hidden;border-radius:4px;box-shadow:0 6px 18px rgba(0,0,0,.18)}
  .card--front{top:210px}
  .card--back{top:630px;background:var(--paper)}
  .card__backdrop{position:absolute;inset:0;background:linear-gradient(135deg,var(--blue-deep) 0%,var(--blue-mid) 55%,var(--blue-light) 100%)}
  .edge-tab{position:absolute;left:0;top:24px;width:40px;height:312px;background:linear-gradient(90deg,var(--green-dark),var(--green));border-radius:0 18px 18px 0}
  .card--front .edge-tab{top:14px;height:332px}
  .brand{position:absolute;display:flex;align-items:center;gap:18px;font-weight:700;color:var(--white);white-space:nowrap}
  .brand__dot{width:34px;height:34px;border-radius:50%;background:var(--green)}
  .card--front .brand{left:160px;top:92px;font-size:84px;letter-spacing:1px}
  .tagline{position:absolute;left:150px;top:230px;color:var(--white);font-size:15px;letter-spacing:.3px;text-transform:uppercase}
  .contact{position:absolute;left:92px;top:76px;font-family:"Cousine",monospace;font-size:19px;line-height:32px;color:var(--ink);font-style:normal}
  .contact__web{margin-top:14px;font-family:"Roboto Condensed",sans-serif;font-size:22px;font-weight:700;color:var(--navy)}
  .divider{position:absolute;left:456px;top:40px;width:1px;height:280px;background:var(--rule)}
  .card--back .brand{left:456px;right:0;top:0;height:360px;flex-direction:column;justify-content:center;gap:16px;color:var(--green);font-size:66px}
  .card--back .brand__dot{width:60px;height:60px}
</style>
</head>
<body>
  <section class="card card--front" aria-label="Frente do cartão">
    <div class="card__backdrop" role="img" aria-label="Fundo azul com curvas suaves decorativas"></div>
    <div class="edge-tab"></div>
    <div class="brand"><span class="brand__dot"></span>Vela Frota Car</div>
    <p class="tagline">A primeira locadora a neutralizar as emissões de carbono em todas as suas operações.</p>
  </section>

  <section class="card card--back" aria-label="Verso do cartão">
    <div class="edge-tab"></div>
    <address class="contact">
      <div>Av. Nome da Avenida 0000,</div>
      <div>Sala 000 - Bairro Centro</div>
      <div>Cidade/UF - Cep: 00000-000</div>
      <div>Tel: 00 0000-0000 / 0000-0000</div>
      <div class="contact__web">www.velafrotacar.com.br</div>
    </address>
    <div class="divider"></div>
    <div class="brand"><span class="brand__dot"></span>Vela Frota Car</div>
  </section>
</body>
</html>
```